Legal Agribusiness Capability Brochure Design

Design A4 sized 6 page Legal Agribusiness Capability Brochure. Design is to be consistent with current marketing materials - logo, letterhead, website and business card to be provided.
Cover page - Firm name and logo, Agribusiness Capability Statement heading with image 1 below
Inside cover page - About Us section with image 2 below then Awards section below image
Inside middle page - Our Expertise with image 3 below
Inside back page - Our Experience with image 4 below
Back page - Senior Lawyers with image 5 below
Outside Middle Back Page - Contact Us with image 6
Updates

To provide more details to designers for brochure

Target Market(s)

Agribusiness - Australia

Industry/Entity Type

Legal

Colors

Designer to choose colors to be used in the design.

Requirements
Must have
• Use content from uloaded file - Agribusiness Brochure Content
• Use images uploaded
• Professional appearance
• Consistent with current marketing and website https://ferngatelegal.com.au/

```html
<!DOCTYPE html>
<html lang="en">
<head>
<meta charset="utf-8">
<title>Ferngate Legal – Agribusiness Capability Statement</title>
<link rel="stylesheet" href="https://fonts.googleapis.com/css2?family=Roboto+Slab:wght@600;700&family=Nunito+Sans:wght@400;600;700&display=swap">
<style>
:root{
  --blue:#3a9be0;
  --ink:#222;
  --bg:#ffffff;
  --seal:#3a3a3a;
  --gold:#e6d27a;
}
*{box-sizing:border-box;margin:0;padding:0}
html,body{width:1200px;height:1200px;overflow:hidden;background:var(--bg)}
body{position:relative;font-family:'Nunito Sans',sans-serif;color:var(--ink)}
.page{position:absolute;width:300px;height:424px;background:#fff;overflow:hidden;box-shadow:0 8px 24px rgba(0,0,0,.13)}
.p1{left:119px;top:161px}.p2{left:450px;top:161px}.p3{left:781px;top:161px}
.p4{left:119px;top:614px}.p5{left:450px;top:614px}.p6{left:781px;top:614px}
.photo{position:absolute;left:0;width:100%}
.photo.top{top:0;height:80px}
.photo.bottom{bottom:0}
.masthead{position:absolute;top:21px;left:21px;right:21px;height:22px;display:flex;align-items:center;justify-content:space-between;z-index:2}
.seal{width:22px;height:22px;border-radius:50%;background:var(--seal)}
.award{width:22px;height:22px;border-radius:50%;background:var(--gold);opacity:.8}
.brand{display:flex;align-items:center;gap:3px}
.brand-mark{width:10px;height:10px;background:var(--blue)}
.brand-name{font-family:'Nunito Sans',sans-serif;font-weight:700;font-size:8px;color:var(--blue);letter-spacing:.3px;text-transform:uppercase}
.content{position:absolute;left:28px;right:26px;z-index:2}
h2{font-family:'Roboto Slab',serif;font-weight:700;color:var(--blue);font-size:8.6px;text-align:center;letter-spacing:.2px;margin:0 0 9px}
p{font-size:5.4px;line-height:1.5;margin:0 0 4px}
ul{list-style:none;margin:0 0 4px}
li{font-size:5.4px;line-height:1.55;padding-left:8px;position:relative}
li::before{content:"";position:absolute;left:1px;top:2.6px;width:2.2px;height:2.2px;border-radius:50%;background:var(--ink)}
.spaced li{line-height:2.15}
.spaced li::before{top:4.6px}
.cover-title{position:absolute;top:110px;left:0;right:0;text-align:center;font-family:'Roboto Slab',serif;font-weight:700;color:var(--blue);font-size:18.5px;line-height:1.38;z-index:2}
.lawyer{display:flex;gap:5px;margin-bottom:3px}
.portrait{flex:0 0 42px;height:50px;background:linear-gradient(#f2f2f2,#b9bfc7)}
.role{font-size:5.6px;color:var(--blue);font-weight:600;text-transform:uppercase;margin-bottom:3px}
.office{font-size:5.6px;color:var(--blue);font-weight:700;margin:9px 0 5px}
.line{display:flex;gap:6px;align-items:flex-start;font-size:5.6px;line-height:1.65;margin-bottom:3px}
.line svg{flex:0 0 6px;width:6px;height:6px;margin-top:1px}
</style>
</head>
<body>

<!-- Cover -->
<section class="page p1">
  <div class="photo" style="top:0;height:100%;background:linear-gradient(#e8d1a8 0%,#efe6d4 28%,#f5efe6 40%,#d9b7a2 55%,#c49a6a 68%,#9c6a3c 80%,#7e3d1c 100%)" role="img" aria-label="Flock of merino sheep standing on red earth farmland under a hazy sky"></div>
  <div class="masthead"><span class="seal"></span><span class="brand"><span class="brand-mark"></span><span class="brand-name">Ferngate Legal</span></span><span class="award"></span></div>
  <h1 class="cover-title">AGRIBUSINESS<br>CAPABILITY STATEMENT</h1>
</section>

<!-- About -->
<section class="page p2">
  <div class="photo top" style="background:linear-gradient(#8fd3ea,#fff)" role="img" aria-label="Clear blue sky"></div>
  <div class="photo bottom" style="height:70px;background:linear-gradient(#fff 0%,#cfe3c2 25%,#7fb860 55%,#d8dc4a 80%,#f0e040 100%)" role="img" aria-label="Green paddocks and yellow canola field"></div>
  <div class="masthead"><span class="seal"></span><span class="brand"><span class="brand-mark"></span><span class="brand-name">Ferngate Legal</span></span><span class="award"></span></div>
  <div class="content" style="top:64px">
    <h2>ABOUT US</h2>
    <ul class="spaced">
      <li>Independent commercial law firm with offices in Geraldton and Perth.</li>
      <li>Senior lawyers offering a combined 65 years of legal experience.</li>
      <li>Practical advice in a professional and timely manner.</li>
      <li>Client relationships built on trust.</li>
      <li>Unfettered access to senior lawyers.</li>
      <li>Direct and ongoing partner level involvement for each client.</li>
      <li>Utilise the best information technology available to maintain high levels of efficiency and confidentiality.</li>
    </ul>
    <h2 style="margin-top:8px">AGRIBUSINESS LEGAL AWARDS</h2>
    <ul class="spaced">
      <li>Ranked as a “Leading Agribusiness Law Firm - Western Australia, 2019” (Top 4)</li>
      <li>Ranked as a “Leading Agribusiness Law Firm - Western Australia, 2018” (Top 4)</li>
      <li>Ranked as a “Leading Agribusiness Law Firm - Western Australia, 2017” (Top 5)</li>
    </ul>
    <h2 style="margin-top:10px">QUALITY PRACTICE STANDARD</h2>
    <p style="line-height:2">We are part of a select group of law firms which has been awarded the Quality Practice Standard by the Western Law Practitioners Council. As a result, we are able to better serve our clients by:</p>
    <ul class="spaced" style="margin-top:8px">
      <li>Adopting modern quality management principles;</li>
      <li>Focusing on clients’ requirements and client care; and</li>
      <li>Striving for consistency of service for all clients by all at the firm.</li>
    </ul>
  </div>
</section>

<!-- Expertise -->
<section class="page p3">
  <div class="photo top" style="height:90px;background:linear-gradient(160deg,#c9a96a 0%,#f3ead6 35%,#8d97a6 70%,#fff 100%)" role="img" aria-label="Sun breaking through a dark sky"></div>
  <div class="photo bottom" style="height:80px;background:linear-gradient(#fff 0%,#c9a46a 25%,#6b5030 60%,#1b140e 100%)" role="img" aria-label="Stockman on horseback mustering cattle at dusk"></div>
  <div class="masthead"><span class="seal"></span><span class="brand"><span class="brand-mark"></span><span class="brand-name">Ferngate Legal</span></span><span class="award"></span></div>
  <div class="content" style="top:64px">
    <h2>EXPERTISE</h2>
    <p>Over several decades our senior lawyers have advised clients involved in wheat, canola, lupin, wool, beef, dairy, wool, lamb, poultry, piggery, viticulture, forestry and plantation businesses.</p>
    <p>Our senior lawyers have strong family connections with pastoralists which allows them to better appreciate the challenges faced in agribusiness.</p>
    <p>Our family connection with pastoralists and our strong technical expertise in agribusiness law places Ferngate Legal in a unique position to advise clients in the agribusiness industry.</p>
    <p>We can assist with the following agribusiness matters:</p>
    <ul class="spaced">
      <li>Agribusiness property contracts, agreements and deeds;</li>
      <li>Sale and purchase of agribusiness and farm assets;</li>
      <li>Pastoral lease advice;</li>
      <li>Native Title advice concerning access and compensation agreements;</li>
      <li>Land access agreements with mining, energy and telecommunications companies;</li>
      <li>Partnership, trust, corporation and joint venture advice;</li>
      <li>Farm Leases, Share Farming Agreements and Livestock Management Agreements;</li>
      <li>Carbon trading advice;</li>
      <li>Mortgages and securities;</li>
      <li>Farm succession planning, including Wills, Enduring Powers of Attorney and Guardianship;</li>
      <li>Employment advice;</li>
      <li>Deceased estates and probate, including advice concerning family provision claims;</li>
      <li>Disputes.</li>
    </ul>
  </div>
</section>

<!-- Experience -->
<section class="page p4">
  <div class="photo top" style="height:85px;background:linear-gradient(#4f8fd0 0%,#9cc4e8 40%,#e9c0b4 55%,#fff 100%)" role="img" aria-label="Blue sky with pink sunset clouds"></div>
  <div class="photo bottom" style="height:68px;background:linear-gradient(#fff 0%,#f6c69a 25%,#ef8a3a 55%,#a8391a 80%,#3a160c 100%)" role="img" aria-label="Outback sunset with windmill and trees"></div>
  <div class="masthead"><span class="seal"></span><span class="brand"><span class="brand-mark"></span><span class="brand-name">Ferngate Legal</span></span><span class="award"></span></div>
  <div class="content" style="top:64px">
    <h2>EXPERIENCE</h2>
    <p style="line-height:1.75">Our senior lawyers have accumulated a wealth of experience in agribusiness law. Most of our work is subject to confidentiality which prevents us from disclosing any confidential information. However, we are able to disclose that our experience in agribusiness includes:</p>
    <ul style="margin-top:7px">
      <li style="line-height:1.75">Advising clients with respect to the sale and acquisition of farmland, including due diligence enquiries, preparation and review of contracts for sale, registration of securities and settlement.</li>
      <li style="line-height:1.75">Advising farmer in relation to the 180-megawatt Coolbrook Wind Farm to be constructed on farmland near Eneabba, with a project value of up to AUD500 million and which is recognised as one of the best renewable projects in Australia.</li>
      <li style="line-height:1.75">Advising pastoral lease holders on the sale and purchase of pastoral leases.</li>
      <li style="line-height:1.75">Advising client on the termination of a vendor terms agreement for the sale of a farm and the repossession and resale of the farm.</li>
      <li style="line-height:1.75">Advising numerous clients on various agreements with mining companies, including Royalty Agreements, Exploration Agreements, Land Access Deeds, Leases, Transmission Line Works Agreements, Deeds of Settlement and Release, Easement Deeds and Lay-Down Area Agreements.</li>
      <li style="line-height:1.75">Advising on Access and Compensation Agreements with native title claimants.</li>
      <li style="line-height:1.75">Advising client in relation to restructure of farmland and the transfer of the farmland to family members, trusts and a SMSF to qualify for the duties exemption under the Duties Act.</li>
      <li style="line-height:1.75">Advising client in relation to the settlement of a farming partnership and trust dispute.</li>
      <li style="line-height:1.75">Advising various farming families / corporate groups in relation to the restructuring of farm assets and exempt family farm transactions under the Duties Act.</li>
      <li style="line-height:1.75">Advising farmers in relation to estate disputes and claims, including claims in the Supreme Court under the Family Provision Act.</li>
    </ul>
  </div>
</section>

<!-- Senior lawyers -->
<section class="page p5">
  <div class="photo top" style="background:linear-gradient(#8fd3ea,#fff)" role="img" aria-label="Clear blue sky"></div>
  <div class="photo bottom" style="height:74px;background:linear-gradient(#fff 0%,#c9a08a 20%,#9a4a2e 50%,#6e6a3a 75%,#3a3224 100%)" role="img" aria-label="Autumn vineyard rows with a dirt track"></div>
  <div class="masthead"><span class="seal"></span><span class="brand"><span class="brand-mark"></span><span class="brand-name">Ferngate Legal</span></span><span class="award"></span></div>
  <div class="content" style="top:64px">
    <h2>EXPERIENCE</h2>
    <div class="lawyer">
      <div class="portrait" role="img" aria-label="Portrait photo of Tom Harlow"></div>
      <div>
        <div class="role">Tom Harlow – Principal</div>
        <p>Tom has practiced exclusively as a commercial lawyer for over 20 years initially at Perth law firms and since 2009 in Geraldton.</p>
        <p>In 2011, Tom established Ferngate Legal in Geraldton and expanded with the opening of a Perth office in 2017.</p>
      </div>
    </div>
    <p>Tom has advised on a large number of commercial matters and disputes, particularly in relation to agribusiness, business, property, wills and estates. He has a proven track record of delivering results to clients, especially in relation to more complex commercial transactions and disputes.</p>
    <p>Tom has a specific interest in agribusiness, primarily due to his family being involved in agribusiness for several generations.</p>
    <p>Ranked by Bennett’s Guide as a:</p>
    <ul style="margin-top:8px">
      <li>“Preeminent Agribusiness Lawyer – Western Australia, 2019” (Top 2 in W.A.)</li>
      <li>“Leading Agribusiness Lawyer – Western Australia, 2018” (Top 5 in W.A.)</li>
      <li>“Leading Agribusiness Lawyer – Western Australia, 2017” (Top 7 in W.A.)</li>
    </ul>
    <div class="lawyer" style="margin-top:6px">
      <div class="portrait" role="img" aria-label="Portrait photo of Max Harlow"></div>
      <div>
        <div class="role">Max Harlow – Consultant</div>
        <p>Max was awarded a Bachelor of Laws from the Western Coast University in 1973. Since then Max has been a partner at firms in Geraldton and Fremantle, as well as a principal of firms in Geraldton and Fremantle. In late 2009 Max and his wife, Ann, made the decision to move back to Geraldton where they had previously lived for approximately 11 years.</p>
      </div>
    </div>
    <p>Max has accumulated experience in a wide range of areas in over 45 years of legal practice, particularly in relation to Agribusiness disputes and litigation, which is of great benefit to his clients.</p>
  </div>
</section>

<!-- Contact -->
<section class="page p6">
  <div class="photo top" style="height:90px;background:linear-gradient(#b39a98 0%,#e7cfc8 45%,#fff 100%)" role="img" aria-label="Soft pink evening sky"></div>
  <div class="photo bottom" style="height:120px;background:linear-gradient(#fff 0%,#f4f0e4 35%,#e8dca0 65%,#c9a84a 85%,#8a7040 100%)" role="img" aria-label="Yellow combine harvester working a grain crop"></div>
  <div class="masthead"><span class="seal"></span><span class="brand"><span class="brand-mark"></span><span class="brand-name">Ferngate Legal</span></span><span class="award"></span></div>
  <div class="content" style="top:64px">
    <h2>CONTACT US</h2>
    <p style="line-height:1.6">If you have any questions or require any assistance in relation to agribusiness law, please contact us at our Geraldton or Perth office.</p>
    <div class="office">Geraldton Office</div>
    <div class="line" style="padding-left:4px"><svg viewBox="0 0 10 10"><path d="M5 0a3.5 3.5 0 0 0-3.5 3.5C1.5 6 5 10 5 10s3.5-4 3.5-6.5A3.5 3.5 0 0 0 5 0zm0 5a1.5 1.5 0 1 1 0-3 1.5 1.5 0 0 1 0 3z" fill="#222"/></svg><span>Suite 4, Harbour View House<br>12 Marina Lane<br>Geraldton WA 6530</span></div>
    <div class="line" style="padding-left:4px"><svg viewBox="0 0 10 10"><rect x="2.5" y="0.5" width="5" height="9" rx="1" fill="none" stroke="#222" stroke-width="1.2"/></svg><span>+61 8 9900 1234</span></div>
    <div class="line" style="padding-left:4px"><svg viewBox="0 0 10 10"><rect x="1" y="3" width="8" height="6" fill="#222"/><rect x="3" y="0.5" width="4" height="3" fill="#222"/></svg><span>+61 8 9900 1235</span></div>
    <div class="line" style="padding-left:4px"><svg viewBox="0 0 10 10"><rect x="0.5" y="2" width="9" height="6" fill="#222"/><path d="M0.5 2 5 5.5 9.5 2" fill="none" stroke="#fff" stroke-width=".8"/></svg><span>info@ferngatelegal.com.au</span></div>
    <div class="office" style="margin-top:14px">Perth Office</div>
    <div class="line" style="padding-left:4px"><svg viewBox="0 0 10 10"><path d="M5 0a3.5 3.5 0 0 0-3.5 3.5C1.5 6 5 10 5 10s3.5-4 3.5-6.5A3.5 3.5 0 0 0 5 0zm0 5a1.5 1.5 0 1 1 0-3 1.5 1.5 0 0 1 0 3z" fill="#222"/></svg><span>88 Kingsway Road<br>West Perth WA 6005</span></div>
    <div class="line" style="padding-left:4px"><svg viewBox="0 0 10 10"><rect x="2.5" y="0.5" width="5" height="9" rx="1" fill="none" stroke="#222" stroke-width="1.2"/></svg><span>+61 8 9300 5678</span></div>
    <div class="line" style="padding-left:4px"><svg viewBox="0 0 10 10"><rect x="1" y="3" width="8" height="6" fill="#222"/><rect x="3" y="0.5" width="4" height="3" fill="#222"/></svg><span>+61 8 9300 5679</span></div>
    <div class="line" style="padding-left:4px"><svg viewBox="0 0 10 10"><rect x="0.5" y="2" width="9" height="6" fill="#222"/><path d="M0.5 2 5 5.5 9.5 2" fill="none" stroke="#fff" stroke-width=".8"/></svg><span>info@ferngatelegal.com.au</span></div>
    <div class="line" style="margin-top:12px"><svg viewBox="0 0 10 10"><circle cx="5" cy="5" r="4.3" fill="none" stroke="#222" stroke-width="1"/><ellipse cx="5" cy="5" rx="1.8" ry="4.3" fill="none" stroke="#222" stroke-width=".8"/><path d="M0.7 5h8.6" stroke="#222" stroke-width=".8"/></svg><span>https://ferngatelegal.com.au/</span></div>
  </div>
</section>

</body>
</html>
```